Landscape Company in need of logo and business card update. Current logo file is attached.

I need a business card design for a Woman Owned Landscape business in Kansas City. I do Native plant installation and maintenance as well as mowing, chemical applications and residential and commercial landscaping.
My colors are navy, green and white.
I currently have a logo that can be used or you can redesign it.

Target Market(s)

Residential and commercial

Industry/Entity Type

Landscape

Contact Information for Business Card

On back of current card it lists what I do and website:
BMP/Raingarden Maintenance and Installation, Certified Chemical Applicator for Trees, shrubs, and turf; Landscape Design and Installation for residential and commercial.

Logo Text

Copperleaf Landscape Services, LLC

Font styles to use
Other font styles liked:
• See current font on logo examples

Requirements
Must have
• Phone number: 816-402-7719
• Website: www.copperleaflandscape-example.com
• Colors: Navy, Green, white
• Email: copperleaflandscape@mailbox-example.com
• Address: PO BOX 471208 Shawnee, KS 66219
• Name of Person: Marcy Dulwick, owner

```html
<!DOCTYPE html>
<html lang="en">
<head>
<meta charset="utf-8">
<title>Copperleaf Landscape Services – Business Card</title>
<link rel="stylesheet" href="https://fonts.googleapis.com/css2?family=Roboto:ital,wght@0,300;0,400;1,700&display=swap">
<style>
  :root {
    --card-white: #ffffff;
    --brand-green: #1fb86a;
    --brand-navy: #1d2f5c;
    --text-grey: #6f7378;
  }
  html, body {
    margin: 0;
    padding: 0;
    width: 800px;
    height: 1200px;
    overflow: hidden;
    background: var(--card-white);
  }
  .business-card {
    position: relative;
    width: 800px;
    height: 1200px;
    background: var(--card-white);
    font-family: "Roboto", Arial, sans-serif;
  }
  .brand {
    position: absolute;
    top: 70px;
    left: 64px;
    display: flex;
    align-items: center;
    gap: 28px;
  }
  .brand-mark {
    width: 150px;
    height: 150px;
    flex: none;
  }
  .brand-name {
    margin: 0;
    max-width: 420px;
    font-size: 30px;
    font-weight: 400;
    line-height: 1.25;
    color: var(--brand-navy);
  }
  .owner {
    position: absolute;
    left: 64px;
    top: 760px;
  }
  .owner-name {
    margin: 0;
    font-size: 72px;
    line-height: 1;
    color: var(--brand-green);
    font-weight: 300;
  }
  .owner-name .surname {
    font-weight: 700;
    font-style: italic;
    text-transform: uppercase;
  }
  .owner-title {
    margin: 10px 0 0;
    font-size: 32px;
    font-weight: 300;
    color: var(--brand-green);
  }
  .contact {
    position: absolute;
    left: 64px;
    top: 960px;
    margin: 0;
    padding: 0;
    list-style: none;
    font-size: 24px;
    font-weight: 300;
    line-height: 1.7;
    color: var(--text-grey);
  }
</style>
</head>
<body>
  <main class="business-card">
    <header class="brand">
      <svg class="brand-mark" viewBox="0 0 150 150" aria-hidden="true">
        <circle cx="75" cy="75" r="72" fill="var(--brand-navy)"/>
      </svg>
      <h1 class="brand-name">Copperleaf Landscape Services, LLC</h1>
    </header>

    <section class="owner">
      <h2 class="owner-name">Marcy <span class="surname">Dulwick</span></h2>
      <p class="owner-title">Owner</p>
    </section>

    <ul class="contact">
      <li>816-402-7719</li>
      <li>PO BOX 471208 Shawnee, KS 66219</li>
      <li>www.copperleaflandscape-example.com</li>
      <li>copperleaflandscape@mailbox-example.com</li>
    </ul>
  </main>
</body>
</html>
```